Cadenza Elite Keyboard Academy is a comprehensive piano studio located in CBD area and provide individual piano lessons.

We also provide services for wedding organising band, or instrumental hiring or venue hiring, or organise concert to students.

I want my name card to be very creative, does not have to be the form or shape with the normal name card, can be in different shape. Also, I want the name card to be very upper class, because learning piano is a serious thing, so I do not want people to bargain with the prices. I want people to see it as a very elegant tuition so that they do not want to bargain and think it is worth to try.

Further more, Cadenza Elite Keyboard Academy is not like normal piano studio only provide piano lessons, we provide band services for each other event, such as cruise party, wedding etc. I want people to see it as owner of Elite Keyboard Academy, they will have different type of services all in one, I provide more than that, and I am well connected. I do not provide only piano lesson, but also all other musical knowledge and I am very professional

I want name card to be very simple, just name of company name, my name and website that's all, maybe phone number and email as well.

Please check my website to have more ideal concept.
http://harrietdowse.sitebuilder-example.com/cadenzakeyboard
Updates

Target Market(s)

For all people who love to play piano (better with upper class)

Industry/Entity Type

Wedding

Contact Information for Business Card

Harriet Dowse
Mobile:0418769052
Email: cadenzaelitekeys@mailbox-example.com

Colors

Designer to choose colors to be used in the design.

Requirements
Must have
• Creativity
Nice to have
• Black and white
some sort of piano image
Should not have
• Childish

```html
<!DOCTYPE html>
<html lang="en">
<head>
<meta charset="UTF-8">
<title>Cadenza Elite Keyboard Academy – Card Holder</title>
<link rel="stylesheet" href="https://fonts.googleapis.com/css2?family=Josefin+Sans:wght@300;400;600&display=swap">
<style>
  :root {
    --backdrop: #e9e7e4;
    --holder-black: #1c1c1c;
    --flap-black: #151515;
    --tab-black: #262626;
    --accent-red: #c8321e;
    --card-white: #fbfbfb;
    --ink: #2a2a2a;
    --ink-soft: #5a5a5a;
    --staff-grey: #b9bec3;
    --key-light: #e6e6e6;
    --key-dark: #9c9c9c;
    --title-white: #f2f2f2;
  }
  * { box-sizing: border-box; margin: 0; padding: 0; }
  html, body { width: 1200px; height: 1000px; overflow: hidden; }
  body {
    background: var(--backdrop);
    font-family: "Josefin Sans", Arial, sans-serif;
    position: relative;
  }

  /* Opened holder: inside view */
  .holder-open {
    position: absolute;
    left: 80px;
    top: 250px;
    width: 520px;
    height: 470px;
    box-shadow: 0 10px 30px rgba(0,0,0,0.25);
  }
  .holder-open .inner-flap {
    height: 170px;
    background: var(--flap-black);
    border-bottom: 1px solid #000;
  }
  .holder-open .pocket {
    position: relative;
    height: 300px;
    background: var(--holder-black);
  }

  .insert-card {
    position: absolute;
    left: 110px;
    top: -60px;
    width: 330px;
    height: 200px;
    background: var(--card-white);
    padding: 22px 22px 0 80px;
    color: var(--ink);
  }
  .insert-card .staff {
    position: absolute;
    left: 14px;
    right: 14px;
    top: 24px;
    height: 60px;
    border-top: 1px solid var(--staff-grey);
    border-bottom: 1px solid var(--staff-grey);
  }
  .insert-card .staff::before,
  .insert-card .staff::after {
    content: "";
    position: absolute;
    left: 0; right: 0;
    border-top: 1px solid var(--staff-grey);
  }
  .insert-card .staff::before { top: 19px; }
  .insert-card .staff::after { top: 39px; }
  .insert-card .clef-mark {
    position: absolute;
    left: 26px;
    top: 16px;
    width: 34px;
    height: 96px;
    border-radius: 17px;
    background: linear-gradient(180deg, #c9ced2, #9aa2a8);
  }
  .insert-card .contact { position: relative; }
  .insert-card .name { font-size: 17px; font-weight: 600; margin-bottom: 6px; }
  .insert-card .line { font-size: 12px; color: var(--ink-soft); line-height: 1.55; font-weight: 400; }
  .insert-card .line.web { font-size: 10.5px; }

  .slot-tab {
    position: absolute;
    left: 150px;
    top: 60px;
    width: 250px;
    height: 80px;
  }

  .keyboard {
    position: absolute;
    left: 0; right: 0; bottom: 0;
    background: linear-gradient(180deg, var(--key-light), #cfcfcf);
    border-top: 4px solid var(--accent-red);
  }
  .holder-open .keyboard { height: 130px; }

  /* Closed holder: front cover */
  .holder-front {
    position: absolute;
    left: 650px;
    top: 360px;
    width: 480px;
    height: 260px;
    background: var(--holder-black);
    box-shadow: 0 10px 30px rgba(0,0,0,0.25);
  }
  .front-title {
    position: absolute;
    left: 0; right: 0;
    top: 34px;
    text-align: center;
    color: var(--title-white);
  }
  .front-title .brand {
    font-size: 34px;
    font-weight: 300;
    letter-spacing: 5px;
  }
  .front-title .tagline {
    display: flex;
    align-items: center;
    justify-content: center;
    gap: 12px;
    margin-top: 6px;
    font-size: 14px;
    font-weight: 300;
    letter-spacing: 3px;
  }
  .front-title .tagline::before,
  .front-title .tagline::after {
    content: "";
    width: 50px;
    border-top: 1px solid var(--title-white);
  }
  .holder-front .keyboard { height: 100px; }
  .holder-front .slot-tab {
    left: 180px;
    top: 132px;
    width: 230px;
    height: 56px;
  }
</style>
</head>
<body>

  <section class="holder-open" aria-label="Card holder, opened">
    <div class="inner-flap"></div>
    <div class="pocket">
      <article class="insert-card">
        <div class="staff"></div>
        <div class="clef-mark" role="img" aria-label="Treble clef on the music staff"></div>
        <div class="contact">
          <p class="name">Harriet Dowse</p>
          <p class="line">0418769052</p>
          <p class="line">cadenzaelitekeys@mailbox-example.com</p>
          <p class="line web">harrietdowse.sitebuilder-example.com/cadenzakeyboard</p>
        </div>
      </article>
      <svg class="slot-tab" viewBox="0 0 250 80" aria-hidden="true">
        <polygon points="0,80 22,0 228,0 250,80" fill="var(--tab-black)"/>
      </svg>
      <div class="keyboard" role="img" aria-label="Piano keyboard band"></div>
    </div>
  </section>

  <section class="holder-front" aria-label="Card holder, front cover">
    <div class="front-title">
      <p class="brand">CADENZA ELITE</p>
      <p class="tagline">KEYBOARD ACADEMY</p>
    </div>
    <div class="keyboard" role="img" aria-label="Piano keyboard band"></div>
    <svg class="slot-tab" viewBox="0 0 230 56" aria-hidden="true">
      <polygon points="0,56 18,0 212,0 230,56" fill="var(--tab-black)"/>
    </svg>
  </section>

</body>
</html>
```